Advertising company unique advertising platform

we need a logo design for a new company based in Australia Melbourne. We develop innovated advertising platform where consumer can use this platform to get regular discount, as business owner they can use this platform for free advertisement. Payment for this advertisement platform only payable every two weeks, when I generate revenue for their business

Industry/Entity Type

Advertising

Contact Information for Business Card

Dale Morrow | Co-Founder |Managing Director
Suite 318 274 Bramwell Lane Melbourne Vic 3000

ABN 62 914 305 718
Tel: +61 0491 258 307 | Email: dale.morrow@plovintarex.com

Font styles to use
Decorative
Script

Requirements
Must have
• Try few different design and some round corner business card
Should not have
• One round corner business card...try 4 different colour background not only black, make sure two side is designed. Be creative so imagine you are giving this to a client make sure has wow factor, if you can also try one design with engrave like all the logo, words look 3d feel
• The word Advertising Platform use attached file font

```html
<!DOCTYPE html>
<html lang="en">
<head>
<meta charset="utf-8">
<title>Tallyfield Market – Business Card</title>
<link href="https://fonts.googleapis.com/css2?family=Quicksand:wght@500;600;700&display=swap" rel="stylesheet">
<style>
  :root {
    --bg: #a9a9a9;
    --front-light: #fdd65c;
    --front-mid: #f4a443;
    --front-deep: #ee6a31;
    --ink: #231f20;
    --back: #2b2a29;
    --accent-yellow: #fcc43e;
    --accent-orange: #f5a23a;
    --accent-red: #e8492c;
    --text-light: #f4f4f4;
  }
  * { box-sizing: border-box; margin: 0; padding: 0; }
  html, body {
    width: 1200px; height: 1200px; overflow: hidden;
    background: var(--bg);
    font-family: "Quicksand", sans-serif;
  }
  .stage {
    position: relative; width: 1200px; height: 1200px;
    display: flex; flex-direction: column; align-items: center; justify-content: center;
    gap: 70px;
  }
  .card {
    position: relative; width: 840px; height: 480px;
    border-radius: 44px; overflow: hidden;
  }

  /* Front */
  .card-front {
    background: linear-gradient(100deg, var(--front-light) 0%, var(--front-mid) 45%, var(--front-deep) 100%);
  }
  .front-swirl {
    position: absolute; left: 40px; top: 40px; width: 340px; height: 420px;
    border-radius: 50% 50% 46% 54% / 40% 44% 56% 60%;
    background: radial-gradient(ellipse at 60% 45%, #ef6d34 0%, #f39a3f 45%, rgba(252, 205, 88, 0.6) 80%, rgba(252, 205, 88, 0) 100%);
    opacity: 0.85;
  }
  .front-brand {
    position: absolute; right: 90px; top: 168px;
    display: flex; align-items: center; gap: 18px;
  }
  .brand-dot {
    width: 54px; height: 54px; border-radius: 50%;
    background: var(--ink);
  }
  .front-brand .brand-name {
    font-weight: 700; font-size: 42px; color: var(--ink); letter-spacing: 0.5px;
  }

  /* Back */
  .card-back { background: var(--back); }
  .back-swirl {
    position: absolute; left: 120px; top: 60px; width: 340px; height: 440px;
    border-radius: 50% 50% 46% 54% / 40% 44% 56% 60%;
    background: radial-gradient(ellipse at 55% 55%, rgba(70, 80, 84, 0.55) 0%, rgba(74, 52, 40, 0.45) 55%, rgba(43, 42, 41, 0) 100%);
  }
  .back-brand {
    position: absolute; left: 60px; top: 176px;
    display: flex; align-items: center; gap: 14px;
  }
  .back-brand .brand-dot { width: 44px; height: 44px; background: var(--accent-orange); }
  .back-brand .brand-name {
    font-weight: 700; font-size: 32px; color: var(--accent-orange);
  }
  .contact {
    position: absolute; left: 440px; top: 120px;
    color: var(--text-light);
  }
  .contact-name {
    font-weight: 600; font-size: 38px; color: var(--accent-yellow); line-height: 1.1;
  }
  .contact-role { font-size: 15px; font-weight: 500; margin-top: 4px; }
  .contact-lines { margin-top: 22px; font-size: 15px; font-weight: 500; line-height: 1.7; }
  .contact-lines .label { color: var(--accent-red); }
  .contact-address { margin-top: 18px; font-size: 15px; font-weight: 500; line-height: 1.7; }
  .edge-band {
    position: absolute; right: 0; bottom: 0; width: 440px; height: 26px;
    background: linear-gradient(90deg, var(--accent-yellow), var(--accent-orange));
  }
</style>
</head>
<body>
<main class="stage">
  <section class="card card-front">
    <div class="front-swirl" role="img" aria-label="Large flowing flame swirl decoration in warm orange tones"></div>
    <div class="front-brand">
      <span class="brand-dot"></span>
      <span class="brand-name">Tallyfield Market</span>
    </div>
  </section>

  <section class="card card-back">
    <div class="back-swirl" role="img" aria-label="Faint flame swirl decoration in dark tones"></div>
    <div class="back-brand">
      <span class="brand-dot"></span>
      <span class="brand-name">Tallyfield Market</span>
    </div>
    <div class="contact">
      <h1 class="contact-name">Dale Morrow</h1>
      <p class="contact-role">Co-Founder | Managing Director</p>
      <p class="contact-lines">
        <span class="label">Tel :</span> +61 0491 258 307<br>
        <span class="label">ABN :</span> 62 914 305 718
      </p>
      <p class="contact-address">
        dale.morrow@plovintarex.com<br>
        Suite 318 274 Bramwell Lane Melbourne Vic 3000
      </p>
    </div>
    <div class="edge-band"></div>
  </section>
</main>
</body>
</html>
```